Corporate Design für Monteur von Photovoltaik-Anlagen
Zielgruppe
Wir sind eine Firma die hauptsächlich Photovoltaik Anlagen und Akkuspeicher/Wallboxen montiert. Unser Hauptaugenmerk liegt bei Privatkunden mit individueller Betreuung. Weiters werden Energiemanagementsysteme angeboten um den selbst erzeugten Strom im Haus wirtschaftlich zu Nutzen.
Aufgabenstellung
Nachhaltigkeit, Vertrauen, Kompetenz sollen das Logo wiedergeben. Ein Themenbezogenes ( Photovoltaik, Stromerzeugung/Autarkie ) symbol und er Firmenname sollten wiedergegeben werden. Die Visitenkarte bzw. das Logo wäre toll wenn es auch fühlbar ist, also erhabener Druck oder geprägt. Auf alle Fälle eine hochwertige Visitenkarte eventuell wie im Anhang mit farbiger Füllung ( rot/Gelb/orange )

```html
<!DOCTYPE html>
<html lang="de">
<head>
<meta charset="utf-8">
<title>Solvanta – Visitenkarten</title>
<link href="https://fonts.googleapis.com/css2?family=Lato:wght@400;700&family=Quicksand:wght@400&display=swap" rel="stylesheet">
<style>
  :root {
    --navy: #1b2340;
    --teal: #1aaa94;
    --panel: #f5f5f5;
    --white: #ffffff;
    --label: #222222;
  }
  * { margin: 0; padding: 0; box-sizing: border-box; }
  html, body { width: 1200px; height: 2400px; overflow: hidden; background: var(--white); }
  body { position: relative; font-family: "Lato", sans-serif; color: var(--navy); }

  .presentation { position: absolute; left: 6px; top: 805px; width: 1194px; height: 788px; background: var(--panel); }
  .variant-label { position: absolute; font-family: "Lato", sans-serif; font-size: 44px; font-weight: 400; color: var(--label); line-height: 1; }
  .variant-label--one { left: 25px; top: 100px; }
  .variant-label--two { left: 22px; top: 454px; }

  .card { position: absolute; width: 390px; height: 251px; box-shadow: 0 8px 18px rgba(0,0,0,0.18); overflow: hidden; }
  .card--front-dark { left: 110px; top: 127px; background: var(--navy); }
  .card--front-light { left: 110px; top: 457px; background: var(--white); }
  .card--back-one { left: 675px; top: 118px; background: var(--white); }
  .card--back-two { left: 675px; top: 437px; background: var(--white); }

  .brand { position: absolute; left: 0; right: 0; top: 0; bottom: 0; display: flex; align-items: center; justify-content: center; gap: 14px; }
  .brand__dot { width: 54px; height: 54px; border-radius: 50%; background: var(--teal); }
  .brand__name { font-family: "Quicksand", sans-serif; font-weight: 400; font-size: 50px; letter-spacing: 1px; line-height: 1; }
  .card--front-dark .brand__name { color: var(--white); }
  .card--front-light .brand__name { color: var(--navy); }

  .back-brand { position: absolute; left: 18px; top: 22px; display: flex; align-items: center; gap: 8px; }
  .back-brand__dot { width: 22px; height: 22px; border-radius: 50%; background: var(--teal); }
  .back-brand__name { font-family: "Quicksand", sans-serif; font-size: 22px; color: var(--navy); line-height: 1; }

  .person { position: absolute; right: 25px; top: 88px; text-align: right; }
  .card--back-two .person { right: 18px; }
  .person__name { font-weight: 700; font-size: 18px; line-height: 20px; color: var(--navy); }
  .person__role { font-weight: 400; font-size: 15px; line-height: 16px; color: var(--navy); }
  .accent-bar { position: absolute; right: 0; top: 90px; width: 9px; height: 38px; background: var(--teal); }

  .address, .contact { position: absolute; top: 183px; font-size: 12px; line-height: 15px; color: var(--navy); list-style: none; }
  .address { left: 18px; }
  .contact { left: 229px; }
  .contact li { display: flex; align-items: center; gap: 5px; }
  .contact svg { width: 10px; height: 10px; flex: none; }
  .footer-band { position: absolute; left: 0; right: 0; bottom: 0; height: 11px; background: var(--navy); }
</style>
</head>
<body>
  <section class="presentation">
    <span class="variant-label variant-label--one">1</span>
    <span class="variant-label variant-label--two">2</span>

    <div class="card card--front-dark">
      <div class="brand"><span class="brand__dot"></span><span class="brand__name">Solvanta</span></div>
    </div>

    <div class="card card--back-one">
      <div class="back-brand"><span class="back-brand__dot"></span><span class="back-brand__name">Solvanta</span></div>
      <div class="person">
        <p class="person__name">Marcus Wendl</p>
        <p class="person__role">Geschäftsführung</p>
      </div>
      <span class="accent-bar"></span>
      <address class="address" style="font-style:normal">Solvanta Energies Systeme GmbH<br>Birkenweg 7<br>6082 Lanzen</address>
      <ul class="contact">
        <li><svg viewBox="0 0 10 10"><path d="M2 1l2 2-1 1c1 1 2 2 3 3l1-1 2 2-1.5 1.5C4 9 1 6 .5 2.5z" fill="none" stroke="var(--teal)" stroke-width="0.8"/></svg>+43 664/25 81 117</li>
        <li><svg viewBox="0 0 10 10"><rect x="1" y="2" width="8" height="6" fill="none" stroke="var(--teal)" stroke-width="0.8"/><path d="M1 2l4 3.5L9 2" fill="none" stroke="var(--teal)" stroke-width="0.8"/></svg>marcus.wendl@solvanta.at</li>
        <li><svg viewBox="0 0 10 10"><circle cx="5" cy="5" r="4" fill="none" stroke="var(--teal)" stroke-width="0.8"/><path d="M1 5h8M5 1c-2 2.5-2 5.5 0 8M5 1c2 2.5 2 5.5 0 8" fill="none" stroke="var(--teal)" stroke-width="0.8"/></svg>www.solvanta.at</li>
      </ul>
      <span class="footer-band"></span>
    </div>

    <div class="card card--front-light">
      <div class="brand"><span class="brand__dot"></span><span class="brand__name">Solvanta</span></div>
    </div>

    <div class="card card--back-two">
      <div class="back-brand"><span class="back-brand__dot"></span><span class="back-brand__name">Solvanta</span></div>
      <div class="person">
        <p class="person__name">Lukas Brenner</p>
        <p class="person__role">technische Leitung</p>
      </div>
      <span class="accent-bar"></span>
      <address class="address" style="font-style:normal">Solvanta Energies Systeme GmbH<br>Birkenweg 7<br>6082 Lanzen</address>
      <ul class="contact">
        <li><svg viewBox="0 0 10 10"><path d="M2 1l2 2-1 1c1 1 2 2 3 3l1-1 2 2-1.5 1.5C4 9 1 6 .5 2.5z" fill="none" stroke="var(--teal)" stroke-width="0.8"/></svg>+43 664 2581 119</li>
        <li><svg viewBox="0 0 10 10"><rect x="1" y="2" width="8" height="6" fill="none" stroke="var(--teal)" stroke-width="0.8"/><path d="M1 2l4 3.5L9 2" fill="none" stroke="var(--teal)" stroke-width="0.8"/></svg>lukas.brenner@solvanta.at</li>
        <li><svg viewBox="0 0 10 10"><circle cx="5" cy="5" r="4" fill="none" stroke="var(--teal)" stroke-width="0.8"/><path d="M1 5h8M5 1c-2 2.5-2 5.5 0 8M5 1c2 2.5 2 5.5 0 8" fill="none" stroke="var(--teal)" stroke-width="0.8"/></svg>www.solvanta.at</li>
      </ul>
      <span class="footer-band"></span>
    </div>
  </section>
</body>
</html>
```